Brenvik - Business Card Design

Design a modern masculine business card for our business

Target Market(s)

Private Market

Industry/Entity Type

Construction

Contact Information for Business Card

Company Name - Name of Person - Address - email address - contact number

Font styles to use
Serif
Sans Serif

Colors
0094D4
00A9DD
6FCCEA
C7EBF8
E9F6FB
00AB8E
00BBA5
67D7C9
C6EFE9
E9F9F6
F0912C
F2A743
F7CA91
FBE8D2
FDF5EE

Requirements
Must have
• Use company logo provided
Nice to have
• Company Logo

```html
<!DOCTYPE html>
<html lang="en">
<head>
<meta charset="utf-8">
<title>Brenvik Construction – Business Card</title>
<link rel="stylesheet" href="https://fonts.googleapis.com/css2?family=Montserrat:wght@400;600;800&display=swap">
<style>
  :root {
    --backdrop: #b4b4b4;
    --card: #1c1c1c;
    --card-back: #181818;
    --orange: #f0702c;
    --white: #ffffff;
    --muted: #3a3a3a;
  }
  * { margin: 0; padding: 0; box-sizing: border-box; }
  html, body { width: 1200px; height: 900px; overflow: hidden; }
  body {
    background: var(--backdrop);
    font-family: "Montserrat", sans-serif;
    position: relative;
  }
  .card {
    position: absolute;
    width: 560px;
    height: 320px;
    border-radius: 22px;
    border-bottom: 4px solid var(--orange);
    border-right: 2px solid var(--orange);
    overflow: hidden;
  }
  .card--back {
    left: 60px; top: 110px;
    background: var(--card-back);
    display: flex; align-items: center; justify-content: center;
  }
  .back-name {
    font-weight: 800;
    font-size: 80px;
    letter-spacing: 3px;
    color: var(--muted);
  }
  .card--front {
    left: 580px; top: 470px;
    background: var(--card);
    color: var(--white);
  }
  .brand {
    position: absolute;
    left: 40px; top: 32px;
    display: flex; align-items: center; gap: 14px;
  }
  .brand-mark {
    width: 22px; height: 22px;
    background: var(--orange);
  }
  .brand-name {
    font-weight: 800;
    font-size: 62px;
    letter-spacing: 2px;
    line-height: 1;
    color: var(--white);
  }
  .brand-sub {
    position: absolute;
    left: 40px; top: 106px;
    font-weight: 600;
    font-size: 15px;
    letter-spacing: 3px;
    color: var(--white);
  }
  .person {
    position: absolute;
    left: 30px; top: 176px;
    width: 260px;
    text-align: right;
  }
  .person-name {
    font-weight: 800;
    font-size: 24px;
    line-height: 1.2;
    color: var(--orange);
  }
  .person-role {
    font-size: 13px;
    margin-bottom: 10px;
  }
  .person-address {
    font-size: 13px;
    line-height: 1.45;
  }
  .divider {
    position: absolute;
    left: 306px; top: 178px;
    width: 1.5px; height: 92px;
    background: var(--orange);
  }
  .contact {
    position: absolute;
    left: 324px; top: 184px;
    list-style: none;
    font-size: 13px;
  }
  .contact li {
    display: flex; align-items: center; gap: 8px;
    margin-bottom: 9px;
    white-space: nowrap;
  }
  .contact svg { width: 14px; height: 14px; fill: var(--orange); flex: none; }
</style>
</head>
<body>

<section class="card card--back" aria-label="Card back">
  <span class="back-name">BRENVIK</span>
</section>

<section class="card card--front" aria-label="Card front">
  <div class="brand">
    <span class="brand-name">BRENVIK</span>
    <span class="brand-mark"></span>
  </div>
  <div class="brand-sub">CONSTRUCTION, INC</div>

  <div class="person">
    <div class="person-name">Daniel Price</div>
    <div class="person-role">Owner</div>
    <div class="person-address">48 Meridian Way, Suite 210<br>Harlow, PA 17402</div>
  </div>

  <div class="divider"></div>

  <ul class="contact">
    <li>
      <svg viewBox="0 0 24 24" aria-hidden="true"><path d="M6.6 10.8a15 15 0 0 0 6.6 6.6l2.2-2.2a1 1 0 0 1 1-.25 11.4 11.4 0 0 0 3.6.57 1 1 0 0 1 1 1V20a1 1 0 0 1-1 1A17 17 0 0 1 3 4a1 1 0 0 1 1-1h3.5a1 1 0 0 1 1 1c0 1.25.2 2.45.57 3.57a1 1 0 0 1-.25 1z"/></svg>
      555-204-7719
    </li>
    <li>
      <svg viewBox="0 0 24 24" aria-hidden="true"><path d="M2 5h20v14H2z M2 5l10 8 10-8" stroke="#1c1c1c" stroke-width="1.5"/></svg>
      info@brenvikconstruction.com
    </li>
    <li>
      <svg viewBox="0 0 24 24" aria-hidden="true"><circle cx="12" cy="12" r="10"/></svg>
      www.brenvikconstruction.com
    </li>
  </ul>
</section>

</body>
</html>
```